Sale of South Sea and Tahitian Pearl Jewellery, online business

I need a business card designed for my website business. We sell South Sea and Tahitian Pearl Jewellery. The colour theme for the website is black and white and would like to carry this through to business cards. Our brand is very elegant and stylish, would like sketch picture of women or fashion involving pearls if not the sketched picture then have the card very plan. below are pictures of the ideas I like and also the logo and writing that is used on my jewellery boxes.
Font is English Hand DB

Target Market(s)

30 and over women in the high end of the market

Industry/Entity Type

Business

Contact Information for Business Card

Business name - Varno Gems( front of card)
Back of card -Details
Rosalind Thackery
Gemmologist MDRS
email: rosalind@varnogems.com.au
website: varnogems.com.au
mob: +61 427 508 193
Perth Australia

Varno Stelle PTY T/AS Varno Gems
ABN 47 283 915 604

Colors
1b1b1b
ffffff
85cae6

Requirements
Must have
• Black and white colour preferably black card with white writing and picture.
• The Same writing as logo and writing on box packaging, attached a file with writing.
• Business name on one side of the card and all other details on the other side.
• Can have tiny hints of the harbour blue colour.
• Font: English Hand DB
Nice to have
• I really like the idea of having a sketch of a stylish or elegent lady wearing pearls or a sketch of a pearl, if not the sketch a really plain and simple card.
Should not have
• busy patterns.

```html
<!DOCTYPE html>
<html lang="en">
<head>
<meta charset="utf-8">
<title>Varno Gems – Business Card</title>
<link href="https://fonts.googleapis.com/css2?family=Montserrat:wght@300;400&display=swap" rel="stylesheet">
<style>
  :root {
    --ink: #000000;
    --paper: #ffffff;
    --harbour: #85cae6;
    --text-dark: #111111;
  }
  * { margin: 0; padding: 0; box-sizing: border-box; }
  html, body {
    width: 1200px; height: 960px; overflow: hidden;
    background: var(--paper);
    font-family: "Montserrat", sans-serif;
  }
  .canvas { position: relative; width: 1200px; height: 960px; }

  .card {
    position: absolute; top: 122px;
    width: 400px; height: 719px;
    overflow: hidden;
  }
  .card--details { left: 147px; }
  .card--brand { left: 657px; background: var(--ink); }

  .details__top {
    position: absolute; left: 0; top: 0;
    width: 400px; height: 360px;
    background: var(--ink);
  }
  .details__bottom {
    position: absolute; left: 0; top: 360px;
    width: 400px; height: 359px;
    background: var(--harbour);
  }

  .seal {
    position: absolute;
    border: 3px solid var(--paper);
    border-radius: 50%;
    display: flex; align-items: center; justify-content: center;
    color: var(--paper);
    font-weight: 300;
    text-align: center;
    line-height: 1.2;
  }
  .seal--details { left: 173px; top: 57px; width: 172px; height: 172px; font-size: 19px; }
  .seal--brand { left: 88px; top: 514px; width: 152px; height: 152px; font-size: 17px; }

  .holder {
    position: absolute; right: 37px; top: 287px;
    text-align: right;
  }
  .holder__name {
    color: var(--paper);
    font-size: 29px; font-weight: 400;
    letter-spacing: 0.2px;
    line-height: 1.1;
  }
  .holder__role {
    color: var(--harbour);
    font-size: 19px; font-weight: 300;
    margin-top: 2px;
  }

  .contact {
    position: absolute; left: 28px; top: 488px;
    display: flex;
  }
  .contact__keys {
    width: 31px; height: 120px;
    background: var(--ink);
    color: var(--paper);
    font-size: 21px; font-weight: 300;
    display: flex; flex-direction: column; align-items: center;
    padding-top: 0;
    line-height: 32.5px;
  }
  .contact__values {
    list-style: none;
    margin-left: 17px;
    color: var(--text-dark);
    font-size: 22px; font-weight: 300;
    line-height: 32.5px;
  }

  .legal {
    position: absolute; left: 28px; top: 644px;
    color: var(--text-dark);
    font-size: 21.5px; font-weight: 300;
    line-height: 27px;
  }

  .figure-art {
    position: absolute; left: 0; top: 0;
    width: 400px; height: 719px;
    background: linear-gradient(160deg, #0b1418 0%, #000000 55%, #06121a 100%);
  }
</style>
</head>
<body>
<main class="canvas">

  <section class="card card--details" aria-label="Card details side">
    <div class="details__top"></div>
    <div class="details__bottom"></div>

    <div class="seal seal--details">Varno Gems</div>

    <div class="holder">
      <p class="holder__name">Rosalind Thackery</p>
      <p class="holder__role">Gemmologist MDRS</p>
    </div>

    <div class="contact">
      <div class="contact__keys" aria-hidden="true">
        <span>e</span><span>w</span><span>m</span>
      </div>
      <ul class="contact__values">
        <li>rosalind@varnogems.com.au</li>
        <li>varnogems.com.au</li>
        <li>+61 427 508 193</li>
        <li>Perth Australia</li>
      </ul>
    </div>

    <p class="legal">Varno Stelle PTY T/AS Varno Gems<br>ABN 47 283 915 604</p>
  </section>

  <section class="card card--brand" aria-label="Card brand side">
    <div class="figure-art" role="img" aria-label="Line sketch of an elegant woman's torso outlined in harbour blue, wearing a pearl necklace"></div>
    <div class="seal seal--brand">Varno Gems</div>
  </section>

</main>
</body>
</html>
```